Business card design for sustainable building and development company

Need a business card design for a new sustainable building and real estate development company in the San Francisco Bay area. Name of company is "Norvale Advisors, LLC" and we provide "Sustainable building, energy and development services" for residential and non residential projects. We'd like the following colors used but not all area required: green, gray, blue. Design should communicate innovation, professionalism and sustainability. Our current website is www.norvale-advisors.example. Another possible design idea is to have the following listed on the back of the card:
Certified: TRAM QX, Leaf Mark Grader, VOLT Grader, EcoState Examiner, RDQ HX Building Analyst. Its not a must but could be text that could be used for back of card. Overall, we are open to a simple, clean design and or one with more text than usual for a card.

Industry/Entity Type

Real Estate

Contact Information for Business Card

Name on card: Dmitri L. Hasby
Title for Name: Principal + Founder
Phone: 555.418.2096
Email: dhasby@norvale-advisors.example
Website: www.norvale-advisors.example

Also, please add the following for address:
San Francisco, California

Requirements
Nice to have
• If you can integrate the outline of a skyline on the backside of the card and if it looks good, I would like to see the design
Should not have
• a barcode;

```html
<!DOCTYPE html>
<html lang="en">
<head>
<meta charset="utf-8">
<title>Norvale Advisors Business Card</title>
<link rel="stylesheet" href="https://fonts.googleapis.com/css2?family=Montserrat:wght@700&family=Oswald:wght@500&family=Open+Sans:wght@400;600&display=swap">
<style>
  :root {
    --green: #6abf4b;
    --charcoal: #222324;
    --white: #ffffff;
    --page: #e9ebe7;
    --ink-light: #f2f2f2;
  }
  * { margin: 0; padding: 0; box-sizing: border-box; }
  html, body { width: 1200px; height: 1018px; overflow: hidden; }
  body {
    background: var(--page);
    font-family: "Open Sans", Arial, sans-serif;
    position: relative;
  }
  .card {
    position: absolute;
    left: 215px;
    width: 770px;
    height: 440px;
    box-shadow: 0 6px 18px rgba(0,0,0,0.18);
    overflow: hidden;
  }
  .card--front { top: 46px; }
  .card--back { top: 532px; }
  .card__art { position: absolute; inset: 0; display: block; }

  .brand {
    position: absolute;
    left: 48px;
    top: 120px;
    display: flex;
    align-items: center;
    gap: 22px;
  }
  .brand__dot {
    width: 86px; height: 86px;
    border-radius: 50%;
    background: var(--green);
    flex: none;
  }
  .brand__name {
    font-family: "Montserrat", Arial, sans-serif;
    font-weight: 700;
    font-size: 44px;
    color: var(--green);
    line-height: 1;
  }
  .brand__tagline {
    margin-top: 8px;
    font-size: 10.5px;
    font-weight: 600;
    letter-spacing: 0.4px;
    text-transform: uppercase;
    color: var(--charcoal);
  }

  .contacts {
    position: absolute;
    left: 48px;
    top: 268px;
    display: grid;
    grid-template-columns: auto auto;
    column-gap: 36px;
    row-gap: 10px;
    color: var(--white);
    font-size: 14px;
  }
  .contacts__item { display: flex; align-items: center; gap: 9px; white-space: nowrap; }
  .contacts__icon { width: 15px; height: 15px; flex: none; }

  .person {
    position: absolute;
    left: 48px;
    top: 356px;
    color: var(--white);
  }
  .person__name {
    font-family: "Oswald", Arial, sans-serif;
    font-weight: 500;
    font-size: 30px;
    letter-spacing: 1px;
    text-transform: uppercase;
    line-height: 1;
  }
  .person__title {
    margin-top: 6px;
    font-size: 13px;
    letter-spacing: 2px;
    text-transform: uppercase;
  }

  .address {
    position: absolute;
    right: 40px;
    top: 366px;
    text-align: right;
    color: var(--ink-light);
    font-size: 16px;
    letter-spacing: 1px;
    line-height: 1.5;
  }
</style>
</head>
<body>

<section class="card card--front" aria-label="Business card front">
  <svg class="card__art" viewBox="0 0 770 440" aria-hidden="true">
    <rect width="770" height="440" fill="var(--white)"/>
    <polygon points="0,250 590,250 650,0 770,0 770,335 0,335" fill="var(--green)"/>
    <polygon points="0,335 770,335 770,440 0,440" fill="var(--charcoal)"/>
    <polygon points="560,335 770,300 770,335" fill="var(--charcoal)"/>
  </svg>

  <div class="brand">
    <span class="brand__dot"></span>
    <div>
      <div class="brand__name">Norvale Advisors</div>
      <div class="brand__tagline">Sustainable building, energy &amp; development services</div>
    </div>
  </div>

  <div class="contacts">
    <div class="contacts__item">
      <svg class="contacts__icon" viewBox="0 0 16 16"><path d="M4 1l2.5 3-1.5 1.5c.8 2 2.5 3.7 4.5 4.5L11 8.5l3 2.5-1.5 3C7 14 2 9 2 2.5z" fill="var(--white)"/></svg>
      555.418.2096
    </div>
    <div class="contacts__item">
      <svg class="contacts__icon" viewBox="0 0 16 16"><rect x="1.5" y="3.5" width="13" height="9" fill="var(--white)"/><path d="M1.5 3.5l6.5 5 6.5-5" stroke="var(--green)" stroke-width="1.4" fill="none"/></svg>
      dhasby@norvale-advisors.example
    </div>
    <div class="contacts__item">
      <svg class="contacts__icon" viewBox="0 0 16 16"><rect x="4" y="1" width="8" height="14" rx="1.5" fill="none" stroke="var(--white)" stroke-width="1.6"/><circle cx="8" cy="12.3" r="0.9" fill="var(--white)"/></svg>
      555.418.2096
    </div>
    <div class="contacts__item">
      <svg class="contacts__icon" viewBox="0 0 16 16"><circle cx="8" cy="8" r="6.5" fill="none" stroke="var(--white)" stroke-width="1.4"/><ellipse cx="8" cy="8" rx="2.8" ry="6.5" fill="none" stroke="var(--white)" stroke-width="1.2"/><path d="M1.5 8h13M3 4.5h10M3 11.5h10" stroke="var(--white)" stroke-width="1.1"/></svg>
      www.norvale-advisors.example
    </div>
  </div>

  <div class="person">
    <div class="person__name">Dmitri L. Hasby</div>
    <div class="person__title">General Manager</div>
  </div>

  <div class="address">San Francisco,<br>California</div>
</section>

<section class="card card--back" aria-label="Business card back">
  <svg class="card__art" viewBox="0 0 770 440" aria-hidden="true">
    <rect width="770" height="440" fill="var(--green)"/>
    <polygon points="150,0 290,0 90,440 -50,440" fill="var(--charcoal)"/>
    <polygon points="560,0 700,0 500,440 360,440" fill="var(--charcoal)"/>
  </svg>
</section>

</body>
</html>
```